Award-winnning Estate Agent needs a premium version of their 'For Sale' board design

We need a premium option for our 'For Sale' board design. We have a standard board that is attached to this brief, but were are looking to have a premium design version that we will use when selling exclusive properties. Our company name is Harbour Lane Estates and the name for this is exclusive selection is: 'The Harbour Collection'. The design needs to work with our current brand, but have a distinctive PREMIUM feel to it. I have uploaded the barnd guidelines and also some of the exisisting logo variations. We do NOT need a new logo but feel free to play around with colours, fonts, sizes etc. for the sign.

Target Market(s)

Property buyers & house hunters

Industry/Entity Type

Real Estate - Residential Property

Font styles to use
Sans Serif

Requirements
Must have
• A premium fee, must be square design, must be easy to read when driving past the sign
Nice to have
• I'm open ot ideas

```html
<!DOCTYPE html>
<html lang="en">
<head>
<meta charset="utf-8">
<title>Harbour Lane Estates – For Sale Board</title>
<link rel="stylesheet" href="https://fonts.googleapis.com/css2?family=Archivo+Black&family=Arimo:wght@700&family=Roboto+Condensed:wght@400;700&display=swap">
<style>
  :root {
    --sale-red: #c4161c;
    --brand-navy: #283891;
    --brand-blue: #1a75bb;
    --board-white: #ffffff;
    --sky-top: #6a93b5;
    --sky-bottom: #7a9fbd;
  }
  * { margin: 0; padding: 0; box-sizing: border-box; }
  html, body {
    width: 1200px;
    height: 622px;
    overflow: hidden;
    background: var(--sky-top);
  }
  .canvas {
    position: relative;
    width: 1200px;
    height: 622px;
  }
  .scene-backdrop {
    position: absolute;
    left: 623px;
    top: 0;
    width: 577px;
    height: 622px;
    background: linear-gradient(180deg, var(--sky-top), var(--sky-bottom));
  }
  .sale-board {
    position: absolute;
    width: 623px;
    height: 622px;
    background: var(--board-white);
    display: flex;
    flex-direction: column;
  }
  .sale-board--main { left: 0; top: 0; }
  .sale-board--display {
    left: 700px;
    top: 150px;
    transform: scale(0.62);
    transform-origin: top left;
    box-shadow: 0 8px 22px rgba(0, 0, 0, 0.25);
  }
  .sale-banner {
    height: 120px;
    background: var(--sale-red);
    color: var(--board-white);
    font-family: "Archivo Black", "Arial Black", sans-serif;
    font-size: 94px;
    line-height: 120px;
    text-align: center;
    letter-spacing: 1px;
  }
  .brand-block {
    height: 246px;
    display: flex;
    flex-direction: column;
    align-items: center;
    justify-content: flex-end;
    padding-bottom: 12px;
    gap: 30px;
  }
  .brand-square {
    width: 110px;
    height: 110px;
    background: var(--brand-blue);
  }
  .brand-name {
    font-family: "Arimo", Arial, sans-serif;
    font-weight: 700;
    font-size: 47px;
    color: var(--brand-navy);
    line-height: 1;
  }
  .collection-band {
    height: 79px;
    background: var(--brand-navy);
    color: var(--board-white);
    font-family: "Roboto Condensed", "Arial Narrow", sans-serif;
    font-weight: 400;
    font-size: 62px;
    line-height: 79px;
    text-align: center;
  }
  .phone-band {
    height: 113px;
    background: var(--brand-blue);
    color: var(--board-white);
    font-family: "Roboto Condensed", "Arial Narrow", sans-serif;
    font-weight: 700;
    font-size: 96px;
    line-height: 113px;
    text-align: center;
    letter-spacing: 1px;
  }
  .web-address {
    flex: 1;
    display: flex;
    align-items: center;
    justify-content: center;
    font-family: "Arimo", Arial, sans-serif;
    font-weight: 700;
    font-size: 36px;
    color: var(--brand-navy);
  }
</style>
</head>
<body>
  <main class="canvas">
    <section class="sale-board sale-board--main" aria-label="For Sale board">
      <header class="sale-banner">FOR SALE</header>
      <div class="brand-block">
        <div class="brand-square" aria-hidden="true"></div>
        <div class="brand-name">Harbour Lane Estates</div>
      </div>
      <div class="collection-band">The Harbour Collection</div>
      <div class="phone-band">01632 960418</div>
      <div class="web-address">www.harbourlaneestates.com</div>
    </section>

    <div class="scene-backdrop" role="img" aria-label="Photograph of the board hanging from a white wooden signpost against a blue sky"></div>

    <section class="sale-board sale-board--display" aria-hidden="true">
      <header class="sale-banner">FOR SALE</header>
      <div class="brand-block">
        <div class="brand-square"></div>
        <div class="brand-name">Harbour Lane Estates</div>
      </div>
      <div class="collection-band">The Harbour Collection</div>
      <div class="phone-band">01632 960418</div>
      <div class="web-address">www.harbourlaneestates.com</div>
    </section>
  </main>
</body>
</html>
```